Professional Financial services company want to rebrand their stationary

We need stationary design for Veltor Group, its a company with 4 member companys that include Veltor Auditing, Veltor Financial Consultancy, Veltor Debt Collection and Veltor Real Estate.

We are based in dubai so the designers need to keep in mind that we use both english and arabic so leave a space for the arabic writing.

We recently redesigned our Logo and would like to redesign our stationary to go along with it.

You will find attached the logo, please keep it looking professional and use the logo as a guide for colors when designing.

Good luck to everyone

Industry/Entity Type

Finance And Accounting

Font styles to use
Sans Serif

Colors
0292cd
33a6d7
3276b5
0355a3
ffffff
dbdbdb

Requirements
Must have
• Letterhead
• Business card
• Envelope small and A4
Nice to have
• Professional
• Space for Arabic and english

```html
<!DOCTYPE html>
<html lang="en">
<head>
<meta charset="utf-8">
<title>Veltor Group – Business Card</title>
<link href="https://fonts.googleapis.com/css2?family=Montserrat:wght@600&family=Source+Sans+3:wght@400;600&family=Tajawal:wght@400;500&display=swap" rel="stylesheet">
<style>
  :root {
    --page-bg: #d9dcdf;
    --card-top: #f4f5f6;
    --card-bottom: #e6e9ec;
    --brand-navy: #1d3a6b;
    --band-deep: #0a3f8f;
    --band-mid: #0355a3;
    --band-light: #3276b5;
    --band-text: #ffffff;
    --band-soft: #c7d6ea;
    --footer-bg: #4a4e55;
    --footer-text: #d6d6d6;
    --footer-label: #e3a48f;
    --rule: #8fb0d6;
  }
  * { margin: 0; padding: 0; box-sizing: border-box; }
  html, body {
    width: 1200px;
    height: 969px;
    overflow: hidden;
    background: var(--page-bg);
  }
  .card {
    position: absolute;
    left: 100px;
    top: 199px;
    width: 1000px;
    height: 571px;
    background: linear-gradient(180deg, var(--card-top), var(--card-bottom));
    box-shadow: 0 10px 30px rgba(0,0,0,0.18);
    overflow: hidden;
  }
  .brand {
    position: absolute;
    left: 0;
    top: 0;
    width: 100%;
    height: 301px;
    display: flex;
    align-items: center;
    justify-content: center;
  }
  .brand-name {
    font-family: "Montserrat", sans-serif;
    font-weight: 600;
    font-size: 68px;
    letter-spacing: -1px;
    color: var(--brand-navy);
    text-transform: uppercase;
    margin-top: 22px;
  }
  .contact-band {
    position: absolute;
    left: 0;
    top: 301px;
    width: 100%;
    height: 178px;
    background: linear-gradient(90deg, var(--band-deep) 0%, var(--band-mid) 55%, var(--band-light) 100%);
    border-bottom: 2px solid var(--rule);
  }
  .arabic-block {
    position: absolute;
    left: 69px;
    top: 10px;
    direction: rtl;
    text-align: left;
    font-family: "Tajawal", sans-serif;
    color: var(--band-text);
  }
  .arabic-block .name { font-size: 38px; font-weight: 500; line-height: 44px; }
  .arabic-block .role { font-size: 30px; font-weight: 500; line-height: 36px; }
  .arabic-block .address { font-size: 25px; line-height: 36px; color: var(--band-soft); }
  .english-block {
    position: absolute;
    right: 35px;
    top: 22px;
    text-align: right;
    font-family: "Source Sans 3", sans-serif;
  }
  .english-block .name { font-size: 28px; font-weight: 600; line-height: 34px; color: var(--band-text); letter-spacing: 0.5px; }
  .english-block .role { font-size: 25px; line-height: 30px; color: var(--band-text); letter-spacing: 0.5px; }
  .english-block .address { font-size: 24px; line-height: 32px; color: var(--band-soft); margin-top: 14px; }
  .footer-band {
    position: absolute;
    left: 0;
    top: 479px;
    width: 100%;
    height: 92px;
    background: var(--footer-bg);
    font-family: "Source Sans 3", sans-serif;
    font-size: 23px;
    color: var(--footer-text);
    text-align: center;
    padding-top: 14px;
    line-height: 32px;
  }
  .footer-band .label { color: var(--footer-label); font-weight: 600; }
  .footer-band .item { margin: 0 6px; }
</style>
</head>
<body>
  <div class="card">
    <div class="brand">
      <span class="brand-name">Veltor Group</span>
    </div>

    <div class="contact-band">
      <div class="arabic-block" lang="ar">
        <div class="name">عمر هادلي</div>
        <div class="role">مؤسس</div>
        <div class="address">4120 هاربرفيو لين</div>
        <div class="address">بروكفيلد، نيويورك 11020</div>
      </div>
      <div class="english-block">
        <div class="name">OMAR HADLEY</div>
        <div class="role">PRESIDENT</div>
        <div class="address">4120 Harborview Lane<br>Brookfield, NY 11020</div>
      </div>
    </div>

    <div class="footer-band">
      <div>
        <span class="item"><span class="label">P:</span> 555 0142 7731</span>
        <span class="item"><span class="label">C:</span> 555 0198 4462</span>
        <span class="item"><span class="label">F:</span> 555 0167 2209</span>
      </div>
      <div>
        <span class="item"><span class="label">E:</span> omar@veltorgroup.com</span>
        <span class="item"><span class="label">W:</span> www.veltorgroup.com</span>
      </div>
    </div>
  </div>
</body>
</html>
```